Business Card design for law firm = Juriskite Australia

We are seeking a new design for our business cards.
We are keeping our logo, which is attached.
We need space for
Name
Title
Address is , which is
Level 14
82 Penhallow Street
Sydney NSW 2000
Phone :
Mobile :
Fax :
Email :
DX :
website www.juriskite.com.au

Industry/Entity Type

Law Firm / Banking and Finance

Contact Information for Business Card

We are seeking a new design for our business cards. We are keeping our logo. We need space for Name Title Address is Level 14 82 Penhallow Street Sydney NSW 2000 Phone Mobile Fax Email DX website www.juriskite.com.au

Colors
0054AA
0677BA
7BADD7
CADEEF
E8F1F8

Requirements
Must have
• see our website for general feel www.juriskite.com.au

```html
<!DOCTYPE html>
<html lang="en">
<head>
<meta charset="utf-8">
<title>Juriskite Australia – Business Cards</title>
<link rel="stylesheet" href="https://fonts.googleapis.com/css2?family=Poppins:wght@400;500;700&display=swap">
<style>
  :root {
    --backdrop: #1e2225;
    --card: #ffffff;
    --brand-deep: #0054aa;
    --brand: #0677ba;
    --brand-light: #7badd7;
    --ink: #1a1a1a;
  }
  * { box-sizing: border-box; margin: 0; padding: 0; }
  html, body {
    width: 1200px; height: 1000px; overflow: hidden;
    background: var(--backdrop);
    font-family: "Poppins", sans-serif;
  }
  .sheet {
    position: relative; width: 1200px; height: 1000px;
    display: flex; align-items: center; justify-content: center; gap: 50px;
  }
  .card {
    position: relative;
    width: 520px; height: 310px;
    background: var(--card);
  }
  .brand {
    color: var(--brand-deep);
    font-weight: 500;
    letter-spacing: .2px;
    line-height: 1;
    white-space: nowrap;
  }

  /* front */
  .card-front .brand { position: absolute; left: 0; right: 0; top: 132px; text-align: center; font-size: 40px; }

  /* back */
  .card-back .brand { position: absolute; left: 34px; top: 40px; font-size: 24px; }
  .divider {
    position: absolute; left: 34px; right: 0; top: 96px;
    height: 1.5px; background: var(--brand);
  }
  .person { position: absolute; left: 34px; top: 112px; }
  .person-name { color: var(--brand); font-weight: 700; font-size: 28px; line-height: 1; }
  .person-title { color: var(--ink); font-size: 10.5px; font-weight: 500; letter-spacing: .4px; margin-top: 3px; }
  .contacts { position: absolute; left: 34px; top: 178px; list-style: none; }
  .contacts li {
    display: flex; align-items: center; gap: 10px;
    font-size: 12.5px; color: var(--ink); height: 21px;
  }
  .contacts .icon { width: 12px; height: 12px; flex: none; color: var(--brand); }
  .dx { font-size: 9px; font-weight: 700; color: var(--brand); width: 12px; }
  .address {
    position: absolute; left: 300px; top: 112px;
    display: flex; gap: 8px; font-size: 12.5px; color: var(--ink); line-height: 1.6;
  }
  .address .icon { width: 11px; height: 14px; color: var(--brand); margin-top: 3px; flex: none; }
</style>
</head>
<body>
<main class="sheet">
  <section class="card card-front" aria-label="Card front">
    <div class="brand">Juriskite</div>
  </section>

  <section class="card card-back" aria-label="Card back">
    <div class="brand">Juriskite</div>
    <div class="divider"></div>
    <div class="person">
      <p class="person-name">NAME</p>
      <p class="person-title">MANAGING DIRECTOR</p>
    </div>
    <ul class="contacts">
      <li><svg class="icon" viewBox="0 0 12 12"><circle cx="6" cy="6" r="6" fill="currentColor"/><path d="M4 3.2l1.2 1.4-.6.8c.4.8 1 1.4 1.8 1.8l.8-.6 1.4 1.2-.8 1C5.8 8.6 3.4 6.2 3.2 4z" fill="#fff"/></svg>02 9460 2187</li>
      <li><svg class="icon" viewBox="0 0 12 12"><rect x="3" y="1" width="6" height="3" fill="currentColor"/><rect x="1" y="4" width="10" height="5" rx="1" fill="currentColor"/><rect x="3" y="7.5" width="6" height="3.5" fill="currentColor" stroke="#fff" stroke-width=".8"/></svg>02 9460 2190</li>
      <li><svg class="icon" viewBox="0 0 12 12"><rect x="1" y="2.5" width="10" height="7" rx="1" fill="currentColor"/><path d="M1.5 3l4.5 3.5L10.5 3" stroke="#fff" stroke-width=".9" fill="none"/></svg>enquiries@juriskite.com.au</li>
      <li><span class="dx">DX</span>318 Sydney</li>
      <li><svg class="icon" viewBox="0 0 12 12" fill="none" stroke="currentColor" stroke-width="1"><circle cx="6" cy="6" r="5"/><ellipse cx="6" cy="6" rx="2.2" ry="5"/><path d="M1 6h10M2 3.5h8M2 8.5h8"/></svg>www.juriskite.com.au</li>
    </ul>
    <div class="address">
      <svg class="icon" viewBox="0 0 11 14"><path d="M5.5 0C2.5 0 0 2.3 0 5.3 0 9 5.5 14 5.5 14S11 9 11 5.3C11 2.3 8.5 0 5.5 0z" fill="currentColor"/><circle cx="5.5" cy="5.3" r="2" fill="#fff"/></svg>
      <p>Level 14, 82 Penhallow Street<br>Sydney NSW 2000</p>
    </div>
  </section>
</main>
</body>
</html>
```